Funeral Comparison Website Needs Designer For WireFrame Mock Up (That we've already done)

This should be a pretty quick design project. It's a single page based on a wireframe mockup we did.
Our site (restfulpathway.example) helps people find and compare funeral homes and cemeteries. Our site hasn't been redesigned since we launched in 2008, so it is fairly dated, and we've seen new competitors pop-up in the past year so we need to come up with a fresh redeisgn. We need someone to take our mockup and work their magic with it. As I mentioned this is a single page based on our wireframe mockup.
Please see attached mockup and logo.
Look and feel
Each slider illustrates characteristics of the customer's brand and the style your logo design should communicate.

```html
<!DOCTYPE html>
<html lang="en">
<head>
<meta charset="utf-8">
<title>RestfulPathway – Request Funeral Quotes</title>
<link rel="stylesheet" href="https://fonts.googleapis.com/css2?family=Ubuntu:wght@400;500;700&display=swap">
<style>
:root{
  --blue:#0b83b4;
  --blue-dark:#0a6f99;
  --green:#2fc800;
  --green-text:#22b800;
  --ink:#111;
  --grey:#555;
  --hero-edge:#d8e7f3;
  --hero-mid:#ffffff;
  --card-line:#d9d9d9;
  --btn:#1b1b1b;
  --red:#b3140c;
}
*{box-sizing:border-box;margin:0;padding:0}
html,body{width:1030px;height:1200px;overflow:hidden;background:#fff}
body{position:relative;font-family:'Ubuntu',Arial,sans-serif;color:var(--ink)}
.abs{position:absolute}

/* header */
.site-header{position:absolute;left:0;top:0;width:1030px;height:95px;border-bottom:1px solid #ddd;background:#fff}
.brand{left:146px;top:46px;display:flex;align-items:center;gap:8px;font-size:22px;font-weight:500;color:var(--blue)}
.brand-dot{width:14px;height:14px;border-radius:50%;background:var(--green)}
.main-nav{left:348px;top:60px;display:flex;font-size:11.5px;letter-spacing:.2px}
.main-nav a{color:#222;text-decoration:none;padding:0 13px;border-right:1px dotted #bbb;line-height:14px}
.main-nav a:last-child{border-right:0}
.social{left:830px;top:56px;display:flex;gap:4px}
.social span{width:20px;height:20px;border-radius:50%;background:var(--green)}

/* hero */
.hero{position:absolute;left:0;top:95px;width:1030px;height:427px;border:1px solid #cfdde8;
  background:radial-gradient(ellipse 60% 70% at 50% 50%,var(--hero-mid) 0%,#eef5fa 50%,var(--hero-edge) 100%)}
.call{right:148px;top:106px;text-align:right}
.call small{display:block;font-size:10.5px;color:#222}
.call strong{display:block;font-size:22px;font-weight:400;letter-spacing:-.5px;line-height:22px}
.hero-title{left:0;width:1030px;top:154px;text-align:center;font-size:33px;font-weight:700;letter-spacing:-1px;line-height:36px}
.hero-sub{left:0;width:1030px;top:189px;text-align:center;font-size:13.5px;font-weight:500;letter-spacing:.4px}
.choice{position:absolute;top:234px;width:238px;height:218px}
.choice svg{position:absolute;inset:0}
.choice p{position:absolute;left:18px;right:18px;top:70px;text-align:center;color:#fff;font-size:19px;font-weight:500;line-height:20px;letter-spacing:-.5px}
.choice.c3 p{top:70px}
.or{position:absolute;top:316px;width:56px;height:56px;border-radius:50%;background:#fff;box-shadow:0 1px 4px rgba(0,0,0,.35);
  display:flex;align-items:center;justify-content:center;font-size:18px;font-weight:500}
.more{right:165px;top:490px;display:flex;align-items:center;gap:8px;font-size:14px}
.more i{width:15px;height:16px;background:var(--red);border-radius:2px;display:flex;align-items:center;justify-content:center}

/* testimonials */
.section-title{font-size:32px;font-weight:700;letter-spacing:-1px}
.testimonials-title{left:149px;top:538px;color:var(--blue)}
.quote{position:absolute;top:596px;width:198px;height:180px;border:1px solid var(--card-line);border-radius:6px;
  background:linear-gradient(135deg,#fff 55%,#ececec 100%);box-shadow:0 1px 3px rgba(0,0,0,.12);padding:14px 10px 0 10px}
.quote .mark{font-size:22px;color:#444;line-height:14px;font-weight:700}
.quote p{font-size:8.6px;line-height:12.5px;color:#333;margin-top:4px}
.quote p b{font-size:15px;line-height:8px}
.quote h4{margin-top:6px;font-size:12px;font-weight:500;color:var(--blue)}
.quote .loc{font-size:10px;color:var(--green-text)}
.tail{position:absolute;top:775px;width:30px;height:22px}
.avatar{position:absolute;top:789px;width:97px;height:97px;border-radius:50%;border:3px solid #a9c4cf;
  background:radial-gradient(circle at 50% 40%,#d9b69a 0%,#8a6e5e 40%,#2a2a2e 80%)}
.btn{position:absolute;top:912px;width:174px;height:38px;border-radius:4px;border:2px solid #000;
  background:repeating-linear-gradient(135deg,#2b2b2b 0 2px,#1a1a1a 2px 4px);color:#fff;
  display:flex;align-items:center;justify-content:center;text-align:center;font-size:12px;font-weight:500;line-height:13px}

/* support */
.support-band{position:absolute;left:0;top:978px;width:1030px;height:40px;background:linear-gradient(#ededed,#fff)}
.support-title{left:150px;top:992px;color:var(--green-text)}
.col{position:absolute;top:1048px}
.col h3{font-size:18px;font-weight:500;color:var(--blue);letter-spacing:-.5px}
.col ul{list-style:none;margin-top:9px}
.col li{font-size:12px;color:#222;line-height:19px;padding-left:15px;position:relative}
.col li::before{content:"»";position:absolute;left:0;font-size:8px;color:#777}
.col-divider{position:absolute;top:1050px;width:1px;height:82px;border-left:1px dotted #bbb}
.footer-rule{left:146px;top:1156px;width:737px;border-top:1px dotted #bbb}
.footer{left:149px;top:1173px;font-size:9px;color:#666}
</style>
</head>
<body>

<header class="site-header">
  <div class="abs brand"><span class="brand-dot"></span>RestfulPathway</div>
  <nav class="abs main-nav">
    <a href="#">HOME</a><a href="#">HOW IT WORKS</a><a href="#">ABOUT US</a><a href="#">CONTACT US</a><a href="#">RESOURCES</a>
  </nav>
  <div class="abs social"><span></span><span></span></div>
</header>

<section class="hero"></section>
<div class="abs call"><small>Give Us A Call</small><strong>800-555-0142</strong></div>
<h1 class="abs hero-title">REQUEST FUNERAL QUOTES</h1>
<div class="abs hero-sub">FREE NO OBLIGATIONS PRICE &amp; SERVICES QUOTES</div>

<div class="choice c1" style="left:155px">
  <svg viewBox="0 0 238 218" width="238" height="218"><path fill="var(--blue)" d="M14 18 Q119 -14 224 18 Q238 22 238 36 V182 Q238 196 224 200 Q119 232 14 200 Q0 196 0 182 V36 Q0 22 14 18 Z"/></svg>
  <p>I Am Planning For The Long Term Future</p>
</div>
<div class="choice c2" style="left:400px">
  <svg viewBox="0 0 238 218" width="238" height="218"><path fill="var(--green)" d="M14 18 Q119 -14 224 18 Q238 22 238 36 V182 Q238 196 224 200 Q119 232 14 200 Q0 196 0 182 V36 Q0 22 14 18 Z"/></svg>
  <p>I Am Planning For A Death That Will Occur Shortly</p>
</div>
<div class="choice c3" style="left:644px">
  <svg viewBox="0 0 238 218" width="238" height="218"><path fill="var(--blue)" d="M14 18 Q119 -14 224 18 Q238 22 238 36 V182 Q238 196 224 200 Q119 232 14 200 Q0 196 0 182 V36 Q0 22 14 18 Z"/></svg>
  <p>A Death Has Just Occured</p>
</div>
<div class="or" style="left:364px">OR</div>
<div class="or" style="left:614px">OR</div>
<div class="abs more">Additional Resources <i><svg width="7" height="5" viewBox="0 0 7 5"><path d="M0 0H7L3.5 5Z" fill="#fff"/></svg></i></div>

<h2 class="abs section-title testimonials-title">Testimonials</h2>

<div class="quote" style="left:203px">
  <div class="mark">&ldquo;</div>
  <p>Lorem ipsum dolor sit amet, consectetuer adipiscing elit, sed diam nonummy nibh euismod tincidunt ut laoreet dolore magna aliquam erat volutpat. Ut wisi enim ad minim veniam, quis nostrud exerci tation ullamcorper suscipit lobortis nisl ut aliquip ex ea commodo consequat. <b>&rdquo;</b></p>
  <h4>DANA WHITFIELD</h4><div class="loc">Philadelphia, PA</div>
</div>
<div class="quote" style="left:416px">
  <div class="mark">&ldquo;</div>
  <p>Lorem ipsum dolor sit amet, consectetuer adipiscing elit, sed diam nonummy nibh euismod tincidunt ut laoreet dolore magna aliquam erat volutpat. Ut wisi enim ad minim veniam, quis nostrud exerci tation ullamcorper suscipit lobortis nisl ut aliquip ex ea commodo consequat. <b>&rdquo;</b></p>
  <h4>MARCUS LEE</h4><div class="loc">Los Angles, CA</div>
</div>
<div class="quote" style="left:630px">
  <div class="mark">&ldquo;</div>
  <p>Lorem ipsum dolor sit amet, consectetuer adipiscing elit, sed diam nonummy nibh euismod tincidunt ut laoreet dolore magna aliquam erat volutpat. Ut wisi enim ad minim veniam, quis nostrud exerci tation ullamcorper suscipit lobortis nisl ut aliquip ex ea commodo consequat. <b>&rdquo;</b></p>
  <h4>ELENA NOVAK</h4><div class="loc">Los Angles, CA</div>
</div>

<svg class="tail" style="left:336px" viewBox="0 0 30 22"><path d="M0 0H30L0 22Z" fill="#f1f1f1" stroke="#d9d9d9"/><path d="M1 0H29" stroke="#f1f1f1" stroke-width="2"/></svg>
<svg class="tail" style="left:549px" viewBox="0 0 30 22"><path d="M0 0H30L0 22Z" fill="#f1f1f1" stroke="#d9d9d9"/><path d="M1 0H29" stroke="#f1f1f1" stroke-width="2"/></svg>
<svg class="tail" style="left:763px" viewBox="0 0 30 22"><path d="M0 0H30L0 22Z" fill="#f1f1f1" stroke="#d9d9d9"/><path d="M1 0H29" stroke="#f1f1f1" stroke-width="2"/></svg>

<div class="avatar" style="left:238px" role="img" aria-label="Portrait photo of the first reviewer"></div>
<div class="avatar" style="left:451px" role="img" aria-label="Portrait photo of the second reviewer"></div>
<div class="avatar" style="left:665px" role="img" aria-label="Portrait photo of the third reviewer"></div>

<a class="btn" style="left:215px">GET STARTED<br>WITH PRE-PLANNING</a>
<a class="btn" style="left:428px">GET STARTED</a>
<a class="btn" style="left:641px">GET STARTED</a>

<div class="support-band"></div>
<h2 class="abs section-title support-title">Support</h2>

<div class="col" style="left:202px">
  <h3>Questions &amp; Answers</h3>
  <ul><li>How We Help?</li><li>How This Work?</li></ul>
</div>
<div class="col-divider" style="left:409px"></div>
<div class="col" style="left:422px">
  <h3>Resourses</h3>
  <ul><li>Advice</li><li>Finances</li><li>Planning Guide</li></ul>
</div>
<div class="col-divider" style="left:621px"></div>
<div class="col" style="left:635px">
  <h3>Get More Help</h3>
  <ul><li style="line-height:12px">Lean About Our Certified<br>Consultant</li></ul>
</div>

<div class="abs footer-rule"></div>
<div class="abs footer">© 2008-2013 restfulpathway.example. All Rights Reserved. Privacy Policy. &nbsp; Contact Us | Home | Partner with RestfulPathway</div>

</body>
</html>
```